BrimKettle international mobile topups web site | ||
Cell phone topup and billing services | ||
Information Technology | ||
www.brimkettle-demo.net | ||
BrimKettle provides payment services and mobile account topups connected to a number of mobile operators. The company facilitates people from developed countries to topup phones of their relatives in developing countries. | ||
The site expresses strong unique image which is consistent with corporate branding and logo (see uploaded files). The design should inspire action, trust, value and intuitiveness for clients. |
Cutting-Edge Unique/Creative Professional Trendy Friendly International Corporate Inspirational Progressive Service Oriented High Tech |
Green (as in logo) | ||
Blue (as in logo) | ||
Shades of Gray | ||
top | ||
www.vandroplex-demo.net | ||
www.korvaset-demo.ru | ||
www.tullwenberg-demo.net | ||

```html
<!DOCTYPE html>
<html lang="en">
<head>
<meta charset="utf-8">
<title>BrimKettle – Global reach, local touch</title>
<link href="https://fonts.googleapis.com/css2?family=Arimo:wght@400;700&family=Caveat:wght@400&display=swap" rel="stylesheet">
<style>
  :root {
    --green: #6cbb3c;
    --green-dark: #4f9a25;
    --green-light: #8fd35d;
    --blue: #1f4f9c;
    --blue-light: #4f7fcf;
    --gray-900: #3c3c3c;
    --gray-700: #5a5a5a;
    --gray-500: #8a8a8a;
    --gray-300: #c9c9c9;
    --gray-200: #e2e2e2;
    --gray-100: #f1f1f1;
    --white: #ffffff;
  }
  * { box-sizing: border-box; margin: 0; padding: 0; }
  html, body { width: 1200px; height: 1099px; overflow: hidden; background: var(--white); }
  body { position: relative; font-family: "Arimo", Arial, sans-serif; color: var(--gray-700); }

  .login-bar {
    position: absolute; left: 748px; top: 0; width: 432px; height: 34px;
    background: linear-gradient(#f4f4f4, #dcdcdc);
    border-radius: 0 0 8px 8px;
    display: flex; align-items: center; gap: 10px; padding: 0 14px;
    font-size: 12px; color: var(--gray-700);
  }
  .login-bar .field {
    width: 130px; height: 20px; background: var(--white); border: 1px solid var(--gray-300);
    border-radius: 3px; font-size: 10px; color: var(--gray-500); padding: 3px 6px;
  }
  .login-bar .go { width: 40px; height: 20px; border-radius: 3px; background: linear-gradient(#f8f8f8, #cfcfcf); border: 1px solid var(--gray-300); }

  .brand { position: absolute; left: 30px; top: 88px; display: flex; align-items: center; gap: 12px; }
  .brand .mark { width: 92px; height: 92px; border-radius: 50%; background: var(--blue); }
  .brand .name { font-size: 46px; font-weight: 700; color: var(--blue); line-height: 1; }
  .brand .tagline { font-size: 20px; font-weight: 700; color: var(--green-dark); margin-top: 6px; white-space: nowrap; }

  .main-nav {
    position: absolute; left: 440px; top: 112px; width: 728px; height: 58px;
    background: linear-gradient(var(--green-light), var(--green-dark));
    border-radius: 8px; box-shadow: 0 3px 6px rgba(0,0,0,.25);
    display: flex; align-items: center; padding: 0 10px;
  }
  .main-nav a {
    color: var(--white); text-decoration: none; font-size: 15px; font-weight: 700;
    padding: 0 22px; height: 58px; line-height: 58px; border-right: 1px solid rgba(255,255,255,.35);
  }
  .main-nav a:last-child { border-right: none; margin-left: auto; }
  .main-nav a.active { background: rgba(255,255,255,.18); }

  .hero {
    position: absolute; left: 30px; top: 238px; width: 1140px; height: 440px;
    background: linear-gradient(#fbfbfb, #e4e4e4);
    border-radius: 10px 10px 0 0;
  }
  .hero h1 { position: absolute; left: 40px; top: 110px; font-size: 48px; font-weight: 700; color: var(--gray-700); letter-spacing: -1px; }
  .hero p { position: absolute; left: 40px; top: 182px; width: 620px; font-size: 18px; line-height: 22px; color: var(--gray-500); }
  .hero .prompt { position: absolute; left: 40px; top: 330px; font-family: "Caveat", cursive; font-size: 24px; color: var(--gray-700); }
  .hero .signup {
    position: absolute; left: 253px; top: 328px; width: 254px; height: 36px; border-radius: 8px;
    background: linear-gradient(var(--blue-light), var(--blue)); color: var(--white);
    font-size: 15px; font-weight: 700; text-align: center; line-height: 36px;
    box-shadow: 0 2px 4px rgba(0,0,0,.3);
  }
  .video {
    position: absolute; left: 720px; top: 84px; width: 398px; height: 244px;
    background: var(--white); border-radius: 10px; box-shadow: 0 4px 12px rgba(0,0,0,.25); padding: 14px;
  }
  .video .screen { width: 100%; height: 100%; background: #0a0a0a; display: flex; align-items: center; justify-content: center; }

  .features {
    position: absolute; left: 30px; top: 678px; width: 1140px; height: 92px;
    background: linear-gradient(#efefef, #d8d8d8); display: flex;
    box-shadow: 0 4px 6px rgba(0,0,0,.12);
  }
  .feature { flex: 1; display: flex; align-items: center; justify-content: center; gap: 12px; font-size: 26px; color: var(--gray-900); white-space: nowrap; }
  .feature.active { background: var(--white); justify-content: flex-start; padding-left: 46px; }
  .feature .accent { color: var(--green-dark); }
  .feature .light { font-weight: 400; color: var(--gray-700); }
  .feature strong { font-weight: 700; }

  .intro { position: absolute; left: 84px; top: 830px; width: 1030px; font-size: 14px; line-height: 19px; color: var(--gray-300); font-style: italic; }

  .site-footer {
    position: absolute; left: 238px; top: 992px; width: 732px; height: 66px;
    background: linear-gradient(#fafafa, #e9e9e9); border-radius: 4px;
    box-shadow: 0 1px 4px rgba(0,0,0,.15);
    display: flex; align-items: center; padding: 0 20px;
  }
  .site-footer .brand-small { display: flex; align-items: center; gap: 8px; font-size: 22px; font-weight: 700; color: var(--blue); }
  .site-footer .brand-small .mark { width: 34px; height: 34px; border-radius: 50%; background: var(--blue); }
  .site-footer .follow { margin-left: auto; font-family: "Caveat", cursive; font-size: 26px; color: var(--gray-700); margin-right: 18px; }
  .site-footer .social { width: 38px; height: 38px; border-radius: 6px; margin-left: 10px; }
  .social.one { background: #1d6fa8; }
  .social.two { background: #3b5a9a; }
  .social.three { background: #5fb6e0; }
  .copyright { position: absolute; left: 0; top: 1072px; width: 1200px; text-align: center; font-size: 12px; color: var(--gray-500); }
</style>
</head>
<body>
  <div class="login-bar">
    <span>User login</span>
    <span class="field">Username</span>
    <span class="field">Password</span>
    <span class="go"></span>
  </div>

  <header class="brand">
    <span class="mark"></span>
    <div>
      <div class="name">BrimKettle</div>
      <div class="tagline">Global reach, local touch</div>
    </div>
  </header>

  <nav class="main-nav">
    <a class="active" href="#">Home</a>
    <a href="#">Products &amp; Solutions</a>
    <a href="#">Customers</a>
    <a href="#">Company</a>
    <a href="#">Contact Us</a>
  </nav>

  <section class="hero">
    <h1>Global reach, local touch</h1>
    <p>BrimKettle provides a quick and interactive gateway to mobile operators for users residing in different countries who wish to top up their own cell phone accounts while travelling abroad, or mobile phones of their relatives residing in other countries.</p>
    <span class="prompt">Not yet a member?</span>
    <span class="signup">Sign Up Free</span>
    <div class="video">
      <div class="screen">
        <svg width="86" height="58" viewBox="0 0 86 58" aria-hidden="true">
          <rect width="86" height="58" rx="8" fill="#5a5a5a"/>
          <path d="M34 16 L56 29 L34 42 Z" fill="#ffffff"/>
        </svg>
      </div>
    </div>
  </section>

  <section class="features">
    <div class="feature active">
      <svg width="36" height="36" viewBox="0 0 36 36" aria-hidden="true"><circle cx="18" cy="18" r="16" fill="#2a2a2a"/><circle cx="18" cy="18" r="10" fill="#e8b923"/></svg>
      <span><strong class="accent">Lorem</strong> <span class="accent">Ipsum</span></span>
    </div>
    <div class="feature">
      <svg width="44" height="30" viewBox="0 0 44 30" aria-hidden="true"><rect x="1" y="1" width="42" height="28" rx="3" fill="none" stroke="#5a5a5a" stroke-width="2"/><circle cx="22" cy="15" r="7" fill="none" stroke="#5a5a5a" stroke-width="2"/></svg>
      <span><strong>Consectetur</strong> <span class="light">Elit</span></span>
    </div>
    <div class="feature">
      <svg width="32" height="32" viewBox="0 0 36 36" aria-hidden="true"><path d="M6 30 L9 21 L26 4 L32 10 L15 27 Z" fill="#3c3c3c"/></svg>
      <span><strong>Adipiscing</strong> <span class="light">Palentesque</span></span>
    </div>
  </section>

  <p class="intro">Lorem ipsum dolor sit amet, consectetur adipiscing elit. Donec consequat blandit bibendum. Fusce euismod nisl ac justo elementum sit amet porttitor nisi malesuada. Suspendisse potenti. Aenean vehicula pharetra ante, ut malesuada massa mattis imperdiet. Maecenas sollicitudin consequat mollis. Donec elementum gravida ligula, in hendrerit turpis faucibus in. Aenean lectus dolor, suscipit ac faucibus quis, posuere vitae tortor. Cras pulvinar nulla sit elit lacinia elementum. Curabitur posuere eleifend nibh quis vehicula.</p>

  <footer class="site-footer">
    <span class="brand-small"><span class="mark"></span>BrimKettle</span>
    <span class="follow">Follow us on ...</span>
    <span class="social one"></span>
    <span class="social two"></span>
    <span class="social three"></span>
  </footer>
  <div class="copyright">BrimKettle © 2011</div>
</body>
</html>
```